Dual (Twin) Wet Wipe Packaging

We are a NY Based Hygiene Brand Specifically for couples, Creating Dual products for Him and Her,
Brand Name is plimora.
Our Initial Product is a single Wet wipe Dual Package with perforated lines one wipe for him and one for her used for after sex.
We Would like to see designs that show a bold modern design with slight edgy to bring out the fun!
The final design Should bring out the idea of couples, connection and bond,

Attached Are photos of color ideas And Attached Design ideas.

The measurement of each half should be 7*9 cm total 14*9 cm with both attached.

```html
<!DOCTYPE html>
<html lang="en">
<head>
<meta charset="utf-8">
<title>plimora – Dual Wipe Sachet Dieline</title>
<link href="https://fonts.googleapis.com/css2?family=Montserrat:wght@400;500;600;700&display=swap" rel="stylesheet">
<style>
  :root {
    --ink-navy: #0f3356;
    --navy-panel: #0f3356;
    --navy-band: #02203f;
    --lavender: #dac6e2;
    --sky: #c9e6f8;
    --pink-band: #d4adc9;
    --white: #ffffff;
    --black: #0b0b0b;
    --rule: #222222;
  }
  * { margin: 0; padding: 0; box-sizing: border-box; }
  html, body { width: 1200px; height: 1200px; overflow: hidden; background: var(--white); }
  body { position: relative; font-family: "Montserrat", sans-serif; }

  .side-title {
    position: absolute; left: 0; width: 1200px; text-align: center;
    color: var(--ink-navy); font-weight: 600; font-size: 24px; letter-spacing: 0.5px;
    transform: translateY(-50%);
  }

  .sachet { position: absolute; left: 238px; width: 730px; height: 469px; display: flex; }
  .sachet--front { top: 78px; }
  .sachet--back { top: 678px; }

  .half { position: relative; width: 365px; height: 100%; overflow: hidden; }
  .half--him { background: var(--navy-panel); color: var(--white); }
  .half--her {
    background: radial-gradient(ellipse 60% 55% at 50% 50%, var(--sky) 0%, #d4dcf0 55%, var(--lavender) 100%);
    color: var(--black);
  }

  .notch {
    position: absolute; top: 14px; width: 22px; height: 12px; border-radius: 50%;
    background: var(--white);
  }
  .notch--left { left: -11px; }
  .notch--right { right: -11px; }

  .line {
    position: absolute; left: 0; width: 100%; text-align: center;
    transform: translateY(-50%); white-space: nowrap;
  }
  .brand { font-weight: 600; font-size: 47px; letter-spacing: 1px; }
  .audience { font-weight: 600; font-size: 30px; letter-spacing: 0.5px; }
  .product { font-weight: 400; font-size: 17px; letter-spacing: 0.3px; }
  .claim { font-weight: 700; font-size: 16px; letter-spacing: 0.4px; }
  .tagline { font-weight: 500; font-size: 15px; letter-spacing: 0.2px; }

  .portrait {
    position: absolute; left: 132px; width: 100px; height: 118px; border-radius: 50px 50px 20px 20px;
  }
  .portrait--him { top: 197px; background: linear-gradient(180deg, #1f4a74, #163d63); }
  .portrait--her { top: 195px; background: linear-gradient(180deg, #b9d4ec, #c5d3ec); }

  .steps-band { position: absolute; left: 0; top: 0; width: 100%; height: 158px; }
  .half--him .steps-band { background: var(--navy-band); }
  .half--her .steps-band { background: var(--pink-band); }
  .step { position: absolute; top: 56px; width: 100px; text-align: center; transform: translateX(-50%); }
  .step svg { display: block; margin: 0 auto; width: 30px; height: 32px; }
  .step-label { display: block; margin-top: 14px; font-size: 19px; font-weight: 400; letter-spacing: 0.4px; }

  .lower-panel { position: absolute; left: 0; top: 158px; width: 100%; height: 311px; }

  .ingredients {
    position: absolute; left: 0; width: 100%; top: 323px;
    display: flex; justify-content: center; font-size: 11px; line-height: 18px; letter-spacing: 0.2px;
  }
  .ingredients-label { font-weight: 600; margin-right: 6px; }
  .ingredients-list { font-weight: 400; width: 196px; }
  .maker { font-size: 11px; font-weight: 400; letter-spacing: 0.2px; }

  .dimensions { position: absolute; left: 0; top: 0; width: 1200px; height: 1200px; pointer-events: none; }
  .dim-label { font-family: "Montserrat", sans-serif; font-size: 9.5px; font-weight: 500; fill: var(--rule); }
</style>
</head>
<body>

  <div class="side-title" style="top:53px;">FRONT SIDE</div>

  <section class="sachet sachet--front">
    <div class="half half--him">
      <span class="notch notch--left"></span>
      <div class="line brand" style="top:97px;">PLIMORA</div>
      <div class="line audience" style="top:166px;">FOR HIM</div>
      <div class="portrait portrait--him" role="img" aria-label="Line illustration of a man's head in profile"></div>
      <div class="line product" style="top:356px;">AFTER INTIMACY WIPE</div>
      <div class="line claim" style="top:389px;">CLEAN &amp; FRESH</div>
    </div>
    <div class="half half--her">
      <span class="notch notch--right"></span>
      <div class="line brand" style="top:97px;">PLIMORA</div>
      <div class="line audience" style="top:166px;">FOR HER</div>
      <div class="portrait portrait--her" role="img" aria-label="Line illustration of a woman's head in profile"></div>
      <div class="line product" style="top:356px;">AFTER INTIMACY WIPE</div>
      <div class="line claim" style="top:389px;">CLEAN &amp; FRESH</div>
    </div>
  </section>

  <div class="side-title" style="top:650px;">BACK SIDE</div>

  <section class="sachet sachet--back">
    <div class="half half--him">
      <div class="steps-band">
        <div class="step" style="left:85px;">
          <svg viewBox="0 0 30 32" fill="none" stroke="currentColor" stroke-width="2.4" stroke-linecap="round" stroke-linejoin="round"><path d="M17 2 L9 12 L15 16 L7 24 L13 30"/><path d="M7 24 L4 27"/></svg>
          <span class="step-label">TEAR</span>
        </div>
        <div class="step" style="left:168px;">
          <svg viewBox="0 0 30 32" fill="none" stroke="currentColor" stroke-width="2.4" stroke-linecap="round" stroke-linejoin="round"><path d="M4 10 Q12 4 20 8 L27 18 Q24 27 15 26 Q6 22 4 14 Z"/><path d="M10 14 Q16 14 20 22"/></svg>
          <span class="step-label">WIPE</span>
        </div>
        <div class="step" style="left:268px;">
          <svg viewBox="0 0 30 32" fill="none" stroke="currentColor" stroke-width="2.4" stroke-linecap="round" stroke-linejoin="round"><path d="M3 7 H27"/><path d="M11 7 V3 H19 V7"/><path d="M5 7 L7 29 H23 L25 7"/><path d="M11 12 V24 M15 12 V24 M19 12 V24"/></svg>
          <span class="step-label">DISPOSE</span>
        </div>
      </div>
      <span class="notch notch--left"></span>
      <div class="lower-panel"></div>
      <div class="line brand" style="top:220px;">PLIMORA</div>
      <div class="line tagline" style="top:264px;">CARE FOR BOTH, TOGETHER.</div>
      <div class="ingredients"><span class="ingredients-label">INGREDIENTS:</span><span class="ingredients-list">WATER, ALOE VERA, FRAGRANCE, CITRIC ACID</span></div>
      <div class="line maker" style="top:386px;">MANUFACTURED BY PLIMORACOP.</div>
      <div class="line maker" style="top:404px;">CITY, STATE, COUNTRY</div>
    </div>
    <div class="half half--her">
      <div class="steps-band">
        <div class="step" style="left:78px;">
          <svg viewBox="0 0 30 32" fill="none" stroke="currentColor" stroke-width="2.4" stroke-linecap="round" stroke-linejoin="round"><path d="M17 2 L9 12 L15 16 L7 24 L13 30"/><path d="M7 24 L4 27"/></svg>
          <span class="step-label">TEAR</span>
        </div>
        <div class="step" style="left:161px;">
          <svg viewBox="0 0 30 32" fill="none" stroke="currentColor" stroke-width="2.4" stroke-linecap="round" stroke-linejoin="round"><path d="M4 10 Q12 4 20 8 L27 18 Q24 27 15 26 Q6 22 4 14 Z"/><path d="M10 14 Q16 14 20 22"/></svg>
          <span class="step-label">WIPE</span>
        </div>
        <div class="step" style="left:261px;">
          <svg viewBox="0 0 30 32" fill="none" stroke="currentColor" stroke-width="2.4" stroke-linecap="round" stroke-linejoin="round"><path d="M3 7 H27"/><path d="M11 7 V3 H19 V7"/><path d="M5 7 L7 29 H23 L25 7"/><path d="M11 12 V24 M15 12 V24 M19 12 V24"/></svg>
          <span class="step-label">DISPOSE</span>
        </div>
      </div>
      <span class="notch notch--right"></span>
      <div class="line brand" style="top:220px;">PLIMORA</div>
      <div class="line tagline" style="top:264px;">CARE FOR BOTH, TOGETHER.</div>
      <div class="ingredients"><span class="ingredients-label">INGREDIENTS:</span><span class="ingredients-list">WATER, ALOE VERA, FRAGRANCE, CITRIC ACID</span></div>
      <div class="line maker" style="top:386px;">MANUFACTURED BY PLIMORACOP.</div>
      <div class="line maker" style="top:404px;">CITY, STATE, COUNTRY</div>
    </div>
  </section>

  <svg class="dimensions" viewBox="0 0 1200 1200" fill="none" stroke="#222" stroke-width="0.8">
    <defs>
      <marker id="tip" viewBox="0 0 6 6" refX="5" refY="3" markerWidth="6" markerHeight="6" orient="auto-start-reverse">
        <path d="M0 0 L6 3 L0 6 Z" fill="#222" stroke="none"/>
      </marker>
    </defs>
    <!-- front -->
    <line x1="985" y1="79" x2="985" y2="295" marker-start="url(#tip)"/>
    <line x1="985" y1="331" x2="985" y2="546" marker-end="url(#tip)"/>
    <text class="dim-label" x="976" y="316" stroke="none">9cm</text>
    <line x1="239" y1="561" x2="406" y2="561" marker-start="url(#tip)"/>
    <line x1="435" y1="561" x2="602" y2="561" marker-end="url(#tip)"/>
    <text class="dim-label" x="408" y="564" stroke="none">7 cm</text>
    <line x1="604" y1="561" x2="771" y2="561" marker-start="url(#tip)"/>
    <line x1="800" y1="561" x2="967" y2="561" marker-end="url(#tip)"/>
    <text class="dim-label" x="773" y="564" stroke="none">7 cm</text>
    <line x1="239" y1="584" x2="575" y2="584" marker-start="url(#tip)"/>
    <line x1="632" y1="584" x2="967" y2="584" marker-end="url(#tip)"/>
    <text class="dim-label" x="588" y="586" stroke="none">14 cm</text>
    <!-- back -->
    <line x1="985" y1="679" x2="985" y2="895" marker-start="url(#tip)"/>
    <line x1="985" y1="931" x2="985" y2="1146" marker-end="url(#tip)"/>
    <text class="dim-label" x="976" y="915" stroke="none">9cm</text>
    <line x1="239" y1="1162" x2="406" y2="1162" marker-start="url(#tip)"/>
    <line x1="435" y1="1162" x2="602" y2="1162" marker-end="url(#tip)"/>
    <text class="dim-label" x="408" y="1165" stroke="none">7 cm</text>
    <line x1="604" y1="1162" x2="771" y2="1162" marker-start="url(#tip)"/>
    <line x1="800" y1="1162" x2="967" y2="1162" marker-end="url(#tip)"/>
    <text class="dim-label" x="773" y="1165" stroke="none">7 cm</text>
    <line x1="239" y1="1181" x2="575" y2="1181" marker-start="url(#tip)"/>
    <line x1="632" y1="1181" x2="967" y2="1181" marker-end="url(#tip)"/>
    <text class="dim-label" x="588" y="1183" stroke="none">14 cm</text>
  </svg>

</body>
</html>
```